Digital Marketing Consultant Needs a Business Card Design

I need a business card to brand myself - I'm a digital marketing consultant, and I do web design, SEO, lead generation, social media, etc. I'm overhauling my website (CorinneHalvorsk.com) and just had a snazzy new logo made.

I like the combo of yellow & gray - I find it eye-catching, upbeat and techie. The exact colors of yellow and gray that I like are #F6BF27 and #6D6D6D. But I'm open to suggestions and other color combinations!

I plan on printing the card using some high-end printing techniques that will ensure the card stands out - either really thick cards with colored edges, or spot UV. Not sure which yet, so if you want to incorporate that into your design, that'd be great!

I'm looking for a clean and modern design, but something that will really stand out when paired with 'fancy' printing.

Target Market(s)

Small and medium-sized business owners.

Industry/Entity Type

Printing

Contact Information for Business Card

Corinne Halvorsk
Digital Marketing
Call or Text: 850-555-0927
Corinne@CorinneHalvorsk.com
www.CorinneHalvorsk.com
@QPZ47 on Chirpline

Font styles to use
Serif
Sans Serif

Requirements
Must have
• My logo, my contact information, and my "company colors" - #F6BF27 and #6D6D6D.
Nice to have
• If there's room to mention all the things that I do:
• Social Media, Web Design, SEO, Lead Generation, Conversion Funnels, PPC
• (don't add if it makes the card cluttered)

```html
<!DOCTYPE html>
<html lang="en">
<head>
<meta charset="utf-8">
<title>Corinne Halvorsk – Business Card</title>
<link href="https://fonts.googleapis.com/css2?family=Cormorant+Garamond:wght@500&family=Open+Sans:ital,wght@0,400;1,400&display=swap" rel="stylesheet">
<style>
  :root {
    --yellow: #F6BF27;
    --gray: #6D6D6D;
    --card: #F4F4F2;
    --backdrop: #DADADA;
  }
  html, body {
    margin: 0;
    width: 1200px;
    height: 900px;
    overflow: hidden;
    background: var(--backdrop);
  }
  .stage {
    position: relative;
    width: 1200px;
    height: 900px;
  }
  .card {
    position: absolute;
    top: 300px;
    width: 520px;
    height: 300px;
    background: var(--card);
    overflow: hidden;
  }
  .card-back { left: 50px; }
  .card-front { left: 630px; }
  .card-shapes {
    position: absolute;
    inset: 0;
  }
  .card-shapes polygon { fill: var(--yellow); }

  /* Back: contact details */
  .contact {
    position: absolute;
    left: 230px;
    top: 92px;
    font-family: "Open Sans", sans-serif;
  }
  .contact-name {
    margin: 0;
    color: var(--yellow);
    font-size: 22px;
    font-weight: 400;
    line-height: 1.1;
  }
  .contact-title {
    margin: 0 0 16px;
    color: var(--yellow);
    font-size: 15px;
    font-style: italic;
  }
  .contact-list {
    list-style: none;
    margin: 0;
    padding: 0;
  }
  .contact-item {
    display: flex;
    align-items: center;
    gap: 10px;
    color: var(--gray);
    font-size: 13.5px;
    line-height: 24px;
  }
  .contact-icon {
    width: 15px;
    height: 15px;
    flex: none;
  }

  /* Front: name mark */
  .brand {
    position: absolute;
    left: 0;
    right: 0;
    top: 108px;
    text-align: center;
  }
  .brand-row {
    display: inline-flex;
    align-items: center;
    gap: 14px;
  }
  .brand-square {
    width: 26px;
    height: 26px;
    border: 2px solid var(--gray);
  }
  .brand-name {
    font-family: "Cormorant Garamond", serif;
    font-weight: 500;
    font-size: 34px;
    letter-spacing: 4px;
    color: var(--gray);
  }
  .brand-rule {
    width: 330px;
    height: 1px;
    margin: 8px auto 6px;
    background: var(--gray);
  }
  .brand-tagline {
    font-family: "Open Sans", sans-serif;
    font-size: 12px;
    letter-spacing: 3px;
    color: var(--gray);
  }
</style>
</head>
<body>
<main class="stage">

  <section class="card card-back" aria-label="Business card back">
    <svg class="card-shapes" viewBox="0 0 520 300" aria-hidden="true">
      <polygon points="0,0 210,0 0,190"/>
    </svg>
    <div class="contact">
      <h1 class="contact-name">Corinne Halvorsk</h1>
      <p class="contact-title">Digital Marketing</p>
      <ul class="contact-list">
        <li class="contact-item">
          <svg class="contact-icon" viewBox="0 0 16 16" aria-hidden="true">
            <circle cx="8" cy="8" r="7" fill="none" stroke="var(--yellow)" stroke-width="1.6"/>
            <path d="M5.5 4.5 L7 6 L6.2 7.2 Q7 9 8.8 9.8 L10 9 L11.5 10.5 L10.5 11.6 Q6 11 4.4 5.5 Z" fill="var(--yellow)"/>
          </svg>
          850-555-0927
        </li>
        <li class="contact-item">
          <svg class="contact-icon" viewBox="0 0 16 16" aria-hidden="true">
            <rect x="1" y="3.5" width="14" height="9" fill="var(--yellow)"/>
            <path d="M1 3.5 L8 9 L15 3.5" fill="none" stroke="var(--card)" stroke-width="1.2"/>
          </svg>
          Corinne@CorinneHalvorsk.com
        </li>
        <li class="contact-item">
          <svg class="contact-icon" viewBox="0 0 16 16" aria-hidden="true">
            <g fill="none" stroke="var(--yellow)" stroke-width="1.4">
              <circle cx="8" cy="8" r="6.5"/>
              <ellipse cx="8" cy="8" rx="3" ry="6.5"/>
              <path d="M1.5 8 H14.5 M2.5 4.8 H13.5 M2.5 11.2 H13.5"/>
            </g>
          </svg>
          www.CorinneHalvorsk.com
        </li>
        <li class="contact-item">
          <svg class="contact-icon" viewBox="0 0 16 16" aria-hidden="true">
            <circle cx="8" cy="8" r="7" fill="var(--yellow)"/>
          </svg>
          @QPZ47 on Chirpline
        </li>
      </ul>
    </div>
  </section>

  <section class="card card-front" aria-label="Business card front">
    <svg class="card-shapes" viewBox="0 0 520 300" aria-hidden="true">
      <polygon points="0,0 250,0 0,95"/>
      <polygon points="520,300 520,225 300,300"/>
    </svg>
    <div class="brand">
      <div class="brand-row">
        <span class="brand-square" aria-hidden="true"></span>
        <span class="brand-name">CORINNE HALVORSK</span>
      </div>
      <div class="brand-rule" aria-hidden="true"></div>
      <div class="brand-tagline">digital marketing</div>
    </div>
  </section>

</main>
</body>
</html>
```